Letter Head Design

I need a letter head design based on my company logo that I attached.
Include phone number: (403)582-4316
Address: 347 14th Avenue NE, Calgary, Alberta, Canada, T3K 4R8

Industry/Entity Type

It Company

```html
<!DOCTYPE html>
<html lang="en">
<head>
<meta charset="utf-8">
<title>Northvale Interiors Corp. – Letterhead</title>
<link href="https://fonts.googleapis.com/css2?family=Open+Sans:wght@400;600;700&display=swap" rel="stylesheet">
<style>
  :root {
    --bg: #ffffff;
    --paper: #ffffff;
    --brand-blue: #0a56a8;
    --brand-blue-light: #1a7fd0;
    --brand-green: #5cb31a;
    --text: #4a4a4a;
    --text-dark: #111111;
    --heading: #7a7a7a;
    --ink: #1a1a1a;
  }
  * { margin: 0; padding: 0; box-sizing: border-box; }
  html, body {
    width: 1200px; height: 1071px; overflow: hidden;
    background: var(--bg);
    font-family: "Open Sans", Arial, sans-serif;
  }
  .letterhead {
    position: absolute; left: 328px; top: 152px;
    width: 543px; height: 767px;
    background: var(--paper);
    overflow: hidden;
  }
  .brand-mark {
    position: absolute; left: 77px; top: 39px;
    width: 80px; height: 80px;
    border: 3px solid var(--brand-green);
    border-radius: 4px;
  }
  .brand-name {
    position: absolute; left: 39px; top: 122px;
    font-size: 25px; font-weight: 600; letter-spacing: -0.5px;
    color: var(--brand-blue);
  }
  .address {
    position: absolute; left: 39px; top: 166px;
    font-size: 8px; line-height: 11px; color: var(--text);
  }
  .phone {
    position: absolute; left: 39px; top: 199px;
    font-size: 8px; color: var(--text);
  }
  .phone b { font-weight: 700; }
  .letter-title {
    position: absolute; left: 125px; top: 241px;
    font-size: 12.5px; font-weight: 700; color: var(--heading);
  }
  .sidebar {
    position: absolute; right: 440px; top: 269px;
    text-align: right; font-size: 8px; line-height: 11px; color: var(--text-dark);
  }
  .sidebar p { margin-bottom: 7px; }
  .sidebar b { font-weight: 700; }
  .body-copy {
    position: absolute; left: 125px; top: 268px; width: 374px;
    font-size: 7.6px; line-height: 11.8px; color: var(--text);
  }
  .body-copy p { margin-bottom: 12px; }
  .closing {
    position: absolute; left: 125px; top: 613px;
    font-size: 7.6px; color: var(--text);
  }
  .signature {
    position: absolute; left: 125px; top: 624px;
    width: 162px; height: 22px;
    background: linear-gradient(90deg, #2a2a2a, #555 60%, #2a2a2a);
    opacity: 0.18; border-radius: 3px;
  }
  .footer-band { position: absolute; left: 0; bottom: 0; width: 543px; height: 62px; }
  .footer-brand {
    position: absolute; left: 361px; top: 722px;
    display: flex; align-items: center; gap: 8px;
  }
  .footer-square { width: 37px; height: 37px; border: 2px solid #fff; border-radius: 3px; }
  .footer-name { font-size: 16px; font-weight: 600; color: #fff; letter-spacing: -0.3px; }
</style>
</head>
<body>
  <main class="letterhead">
    <div class="brand-mark"></div>
    <div class="brand-name">Northvale</div>

    <div class="address">347 14th Avenue NE, Calgary, Alberta,<br>Canada, T3K 4R8</div>
    <div class="phone"><b>phone</b>: (403)582-4316</div>

    <h1 class="letter-title">Lorem ipsum</h1>

    <aside class="sidebar">
      <p><b>Lorem ipsum</b><br>dolor sit amet.</p>
      <p><b>Lorem</b><br>ipsum dolor sit</p>
      <p><b>Lorem</b><br>ipsum</p>
    </aside>

    <section class="body-copy">
      <p>Dolor sit amet, consectetur adipiscing elit. Morbi ut ipsum sit amet ipsum sodales venenatis at et arcu. Sed feugiat enim vitae bibendum condimentum. Aliquam vel mattis mauris. Aliquam nec dolor at neque rhoncus aliquam. Nam fringilla condimentum lacus, et posuere purus imperdiet ac. Suspendisse nisl eros, rhoncus a vestibulum vitae, fringilla in sem. Cras nec mauris nec leo viverra euismod in vel odio. In pellentesque dolor eu nunc tincidunt mollis. Mauris dignissim lectus at mauris egestas, in pharetra nisi hendrerit. Aenean sit amet ante sollicitudin, facilisis orci sit amet, dictum dolor. Nullam bibendum feugiat turpis, vitae aliquet nisi porttitor id. Vivamus erat lorem, imperdiet sed nulla sodales, sagittis lacinia urna. In a tristique felis. Ut dui diam, rhoncus eget gravida sit amet, convallis at eros. Integer cursus nec sem et lacinia.</p>
      <p>Nunc ligula odio, iaculis at ante eget, tincidunt adipiscing ante. Vestibulum mattis sapien dolor, porta porttitor urna dapibus sed. Nunc egestas ipsum et arcu fermentum, eget vulputate nunc semper. Ut volutpat venenatis porttitor. Proin accumsan cursus nisl et condimentum. Praesent tempus sapien quis augue feugiat, vitae auctor risus scelerisque. Nulla vehicula, dui in commodo lobortis, massa mi convallis mi, sit amet pellentesque ligula lorem at erat. Praesent porttitor lectus quis felis consectetur, id auctor dolor commodo. Curabitur dictum, libero in aliquam tincidunt, nunc tellus pretium tellus, sed facilisis magna dui at eros. Ut at orci aliquam, tincidunt nibh interdum, auctor ipsum. Ut molestie orci nec lectus vehicula vestibulum.</p>
      <p>Maecenas accumsan, augue et luctus semper, massa nulla fermentum est, ac dictum tellus lacus in erat. Aliquam tristique, augue et tristique ultricies, dui urna commodo justo, id convallis purus magna quis urna. Class aptent taciti sociosqu ad litora torquent per conubia nostra, per inceptos himenaeos. Vestibulum quis nibh nec arcu fringilla sollicitudin sed nec odio. Vestibulum adipiscing ligula sit amet lorem iaculis, quis venenatis turpis rhoncus. Praesent vitae pellentesque odio. Phasellus at magna luctus risus consectetur lobortis. Aliquam ac ultricies lorem, eget lobortis ante. Donec et nisl et sem ultrices hendrerit. In ullamcorper vitae enim non auctor. Fusce pharetra magna nec nisi laoreet iaculis. Phasellus rutrum lorem in leo dictum hendrerit. Praesent a mauris nec eros tempor facilisis.</p>
    </section>

    <div class="closing">Fusce scelerisque</div>
    <div class="signature" role="img" aria-label="Handwritten signature"></div>

    <svg class="footer-band" viewBox="0 0 543 62" aria-hidden="true">
      <defs>
        <linearGradient id="bandFill" x1="0" y1="0" x2="0" y2="1">
          <stop offset="0" stop-color="var(--brand-blue-light)"/>
          <stop offset="1" stop-color="var(--brand-blue)"/>
        </linearGradient>
      </defs>
      <rect x="0" y="47" width="543" height="15" fill="var(--brand-blue)"/>
      <polygon points="299,47 347,0 543,0 543,62 299,62" fill="url(#bandFill)"/>
    </svg>
    <div class="footer-brand">
      <div class="footer-square"></div>
      <div class="footer-name">Northvale</div>
    </div>
  </main>
</body>
</html>
```